Polystyrene Recycling Material Flow

We need a diagram styled as an infographic that shows how polystyrene foam is recycled starting with a manufactured product, moving through the distribution process, waste material collection and reincorporation back into manufacturing. This is accomplished in different ways once the material is collected which needs to be clearly evident. The most important thing is for it to be simple enough to understand while still having a stylish look. The design can be with or without vector images or photography to depict the different stages. We are providing a very rudimentary 'sketch' of the information points and movement flow. Please see www.foamtradeunion.org (resources) to view our literature branding. The RGB & CMYK are attached.

Target Market(s)

Government Agencies, Brand Owners, Retailers, Recycling Industry

Industry/Entity Type

Packaging, Recycling, Manufacturing

Font styles to use
Sans Serif

Requirements
Must have
• Easy to Understand
Nice to have
• Images - either photography or vector illustrations - are optional. We have provided examples of both to show what could be used but are not required. Substituting your own interpretation of imagery is encouraged.
Should not have
• Outdated look.

```html
<!DOCTYPE html>
<html lang="en">
<head>
<meta charset="utf-8">
<title>Recycling Polystyrene Foam</title>
<link rel="stylesheet" href="https://fonts.googleapis.com/css2?family=Montserrat:wght@800;900&family=Lexend:wght@300;400&display=swap">
<style>
  :root{
    --cream:#fbfbe6;
    --panel:#f2f1cd;
    --olive:#9fa02a;
    --gold:#c0901c;
    --gold-deep:#b98a2a;
    --brown:#5a2a12;
    --text-brown:#5b3016;
    --orange:#f6a21e;
    --steel:#5f8ca8;
    --tan:#dcc88a;
    --line:#6b4a2a;
    --dash:#c9a54f;
  }
  *{box-sizing:border-box;margin:0;padding:0}
  html,body{width:886px;height:1200px;overflow:hidden}
  body{background:var(--cream);font-family:"Lexend",sans-serif;color:var(--text-brown);position:relative}
  .abs{position:absolute}
  .heavy{font-family:"Montserrat",sans-serif;font-weight:900;letter-spacing:-0.02em;line-height:1}
  .light{font-weight:300;line-height:1.05;white-space:nowrap}

  .badge{left:52px;top:52px;width:292px;height:90px;background:var(--olive);border-radius:10px;transform:rotate(-3deg);
    color:#fff;font-size:50px;display:flex;align-items:center;justify-content:center;box-shadow:0 4px 8px rgba(0,0,0,.12)}
  .headline{left:62px;top:144px;color:var(--gold);font-size:58px}
  .brand{left:582px;top:71px;display:flex;align-items:center;gap:12px}
  .brand-dot{width:124px;height:124px;border-radius:50%;background:var(--gold)}
  .brand-name{font-size:24px;font-weight:400;color:#2b2417;line-height:1.05}

  .panel{background:var(--panel);border-radius:10px}
  .dashed{border:2px dashed var(--dash);border-radius:12px}
  .art{border-radius:8px}

  .sources{left:61px;top:287px;width:378px;height:354px;background:#f3f2d2}
  .sources-title{left:85px;top:311px;font-size:34px;color:var(--brown)}
  .src{font-size:23px}
  .chan{font-size:18px;line-height:1.15}

  .step-title{font-family:"Montserrat",sans-serif;font-weight:900;color:var(--brown);letter-spacing:-0.02em;line-height:1;white-space:nowrap}
  .gold-box{background:var(--gold-deep);color:#fff;border-radius:10px}

  .collection{left:233px;top:689px;width:419px;height:77px;background:var(--orange);border-radius:8px;color:#fff;
    font-size:50px;display:flex;align-items:center;justify-content:center}

  .compaction{left:148px;top:833px;width:229px;height:136px;background:var(--steel);border-radius:10px;color:#fff}
  .arrow-down{font-size:20px;color:var(--line);left:612px}
</style>
</head>
<body>

<svg class="abs" width="886" height="1200" style="left:0;top:0" aria-hidden="true">
  <g fill="none" stroke="var(--line)" stroke-width="1">
    <path d="M205 413H257M257 393V430M257 393H290M257 430H290"/>
    <path d="M262 554V598M262 554H294M262 598H294"/>
    <path d="M437 857V1121M411 857H437M411 1121H437M437 867H452M437 974H452M437 1083H452"/>
  </g>
  <g fill="none" stroke="var(--line)" stroke-width="1" stroke-dasharray="3 2">
    <path d="M175 428H212V458"/>
    <path d="M181 507H249V564H241"/>
    <path d="M485 418H544V361H600"/>
    <path d="M458 450H511V511H540"/>
    <path d="M254 686H200V745"/>
    <path d="M598 678H647V611"/>
    <path d="M598 702H647V792"/>
  </g>
  <g fill="var(--line)">
    <path d="M452 863L459 867L452 871Z M452 970L459 974L452 978Z M452 1079L459 1083L452 1087Z"/>
  </g>
  <g fill="#111">
    <circle cx="248" cy="686" r="5"/><circle cx="204" cy="772" r="5"/>
    <circle cx="638" cy="678" r="5"/><circle cx="638" cy="702" r="5"/>
    <circle cx="682" cy="653" r="5"/><circle cx="682" cy="793" r="5"/>
  </g>
</svg>

<div class="abs badge heavy">Recycling</div>
<div class="abs headline heavy">POLYSTYRENE<br>FOAM</div>

<div class="abs brand">
  <div class="brand-dot"></div>
  <div class="brand-name">Foam Trade<br>Union</div>
</div>

<!-- Waste sources -->
<div class="abs sources dashed"></div>
<div class="abs sources-title heavy">EPS WASTE<br>SOURCES</div>
<div class="abs art" role="img" aria-label="Green garbage truck illustration" style="left:337px;top:298px;width:192px;height:75px;background:linear-gradient(90deg,#e6e6e6 0 22%,#3aa04a 22%)"></div>
<div class="abs src light" style="left:85px;top:389px">Municipal<br>Waste</div>
<div class="abs src light" style="left:85px;top:468px">Manufacturing<br>Waste</div>
<div class="abs src light" style="left:85px;top:550px">Commercial<br>Waste</div>
<div class="abs chan light" style="left:302px;top:389px">Curbside<br>Collection</div>
<div class="abs chan light" style="left:302px;top:446px">Drop-Off<br>Centers</div>
<div class="abs chan light" style="left:302px;top:544px">Back Hauling</div>
<div class="abs chan light" style="left:302px;top:578px">Localized<br>Delivery</div>
<div class="abs art" role="img" aria-label="Green waste bin filled with mixed refuse" style="left:178px;top:577px;width:103px;height:80px;background:linear-gradient(180deg,#e9a13a 0 28%,#5cb83a 28%)"></div>

<!-- Regrind -->
<div class="abs panel" style="left:564px;top:260px;width:222px;height:71px"></div>
<div class="abs step-title" style="left:581px;top:273px;font-size:22px">REGRIND</div>
<div class="abs light" style="left:581px;top:298px;font-size:21px">Molder Facilities</div>
<div class="abs art" role="img" aria-label="Conveyor feeding a grinding machine" style="left:606px;top:324px;width:222px;height:71px;background:linear-gradient(90deg,#b9b43a,#8a8f98)"></div>

<!-- Shredding -->
<div class="abs panel" style="left:541px;top:422px;width:234px;height:138px"></div>
<div class="abs step-title" style="left:554px;top:436px;font-size:22px">SHREDDING</div>
<div class="abs light" style="left:566px;top:462px;font-size:21px">Homogenization</div>
<div class="abs light" style="left:566px;top:496px;font-size:21px">Mixing of<br>Consistency</div>
<div class="abs art" role="img" aria-label="Green industrial shredder with chopped foam" style="left:764px;top:419px;width:89px;height:152px;background:linear-gradient(180deg,#b4584a 0 18%,#6aa23e 18%)"></div>
<div class="abs gold-box heavy" style="left:541px;top:571px;width:258px;height:63px;padding:10px 0 0 12px;font-size:19px;line-height:1.1">RECYCLED CONTENT<br>PACKAGING &lt;= 15%</div>

<div class="abs collection heavy">COLLECTION</div>

<!-- Compaction -->
<div class="abs dashed" style="left:73px;top:812px;width:321px;height:352px"></div>
<div class="abs art" role="img" aria-label="Blue hydraulic compaction press" style="left:67px;top:778px;width:101px;height:142px;background:linear-gradient(180deg,#2f6fc0,#1f4d94)"></div>
<div class="abs compaction"></div>
<div class="abs heavy" style="left:192px;top:848px;font-size:21px;color:#fff">COMPACTION</div>
<div class="abs light" style="left:202px;top:873px;font-size:20px;color:#fff">Extruded Ingot</div>
<div class="abs light" style="left:202px;top:904px;font-size:20px;color:#fff">Hydraulic<br>Compression</div>

<div class="abs panel" style="left:78px;top:990px;width:278px;height:67px;background:#ece9b6"></div>
<div class="abs art" role="img" aria-label="Stacked white rigid foam boards" style="left:44px;top:994px;width:109px;height:89px;background:linear-gradient(135deg,#ffffff,#d6d6d0)"></div>
<div class="abs step-title" style="left:168px;top:1003px;font-size:19px">EXTRUDED<br>RIGID PS PELLET</div>
<div class="abs panel" style="left:153px;top:1079px;width:205px;height:68px;background:var(--tan)"></div>
<div class="abs step-title" style="left:172px;top:1092px;font-size:19px">END MARKET<br>APPLICATIONS</div>

<!-- Resin path -->
<div class="abs panel" style="left:470px;top:833px;width:324px;height:75px"></div>
<div class="abs step-title" style="left:485px;top:848px;font-size:19px">RECYCLED CONTENT<br>EPS RESIN</div>
<div class="abs" role="img" aria-label="Pile of white recycled resin beads" style="left:743px;top:793px;width:88px;height:85px;border-radius:50%;background:radial-gradient(circle at 40% 40%,#ffffff,#cfcfca)"></div>
<div class="abs arrow-down" style="top:910px">↓</div>
<div class="abs dashed" style="left:470px;top:939px;width:300px;height:75px;border-color:var(--dash)"></div>
<div class="abs step-title" style="left:485px;top:955px;font-size:19px">RE-PELLETIZED<br>WITH BLOWING AGENT</div>
<div class="abs arrow-down" style="top:1015px">↓</div>
<div class="abs gold-box heavy" style="left:470px;top:1043px;width:380px;height:111px;padding:15px 0 0 14px;font-size:21px;line-height:1.2">EXPANDED POLYSTYRENE<br>PACKAGING &amp; BUILDING<br>PRODUCTS ≤50%</div>

</body>
</html>
```